Kestrel Lane flyer

Need a A6 size horizontal layout flyer. See attached example for ideas as well as some images I have which you can use. we are a hire car company that provides vehicles to clients who have recently been involved in car accidents and who's cars are currently getting fixed and so they lose the use of their own vehicle. see our website to keep flyer in line with website and for any further information kestrellane.com.au

Target Market(s)

people involved in not at fault car accidents

Industry/Entity Type

It Company

Requirements
Must have
• *ask people to let us know where they got our flyer from when they call us
• *call to action for people to call our phone number 1800 417 582
Should not have
• any mentioning that the vehicle is free

```html
<!DOCTYPE html>
<html lang="en">
<head>
<meta charset="utf-8">
<title>Kestrel Lane – Rent a Car Flyer</title>
<link rel="stylesheet" href="https://fonts.googleapis.com/css2?family=Oswald:wght@500;600;700&family=Lato:wght@400;700;900&family=Montserrat:wght@800&display=swap">
<style>
  :root {
    --blue: #2f6fbd;
    --blue-deep: #1d56a3;
    --blue-light: #6aa6de;
    --orange: #f7941d;
    --orange-light: #fbb63b;
    --ink: #1c1c1c;
    --white: #ffffff;
    --page: #e6e6e6;
    --yellow-dot: #f6b31c;
  }
  * { margin: 0; padding: 0; box-sizing: border-box; }
  html, body {
    width: 1200px; height: 902px; overflow: hidden;
    background: var(--page);
  }
  .flyer {
    position: absolute; left: 0; top: 43px;
    width: 1200px; height: 816px;
    background: var(--white);
    overflow: hidden;
    font-family: "Lato", sans-serif;
  }
  .flyer-shapes { position: absolute; inset: 0; }
  .brand-name {
    position: absolute; left: 0; width: 478px; top: 108px;
    text-align: center;
    font-family: "Lato", sans-serif; font-weight: 900;
    font-size: 42px; color: var(--ink);
  }
  .headline {
    position: absolute; left: 618px; top: 296px;
    font-family: "Oswald", sans-serif; font-weight: 600;
    font-size: 94px; line-height: 1; color: var(--blue);
  }
  .subhead {
    position: absolute; left: 620px; top: 410px;
    font-family: "Oswald", sans-serif; font-weight: 500;
    font-size: 40px; line-height: 1; color: var(--ink);
  }
  .offer {
    position: absolute; left: 34px; top: 458px; width: 364px;
    text-align: center; color: var(--white);
    font-family: "Oswald", sans-serif;
  }
  .offer-title { font-size: 42px; font-weight: 600; line-height: 1; }
  .offer-deal {
    display: flex; align-items: center; justify-content: center;
    gap: 6px; margin-top: 8px; color: var(--ink);
  }
  .offer-percent { font-size: 70px; font-weight: 700; line-height: 1; }
  .offer-off {
    writing-mode: vertical-rl; transform: rotate(180deg);
    font-size: 30px; font-weight: 700; line-height: 1;
  }
  .offer-period { font-size: 28px; font-weight: 600; line-height: 0.95; text-align: left; }
  .plan {
    position: absolute; top: 666px; width: 116px; text-align: center;
    font-family: "Oswald", sans-serif; color: var(--white);
    text-shadow: 0 1px 2px rgba(0,0,0,.45);
  }
  .plan-name { font-size: 14px; font-weight: 500; line-height: 1.2; color: var(--ink); text-shadow: none; }
  .plan-price { font-size: 40px; font-weight: 700; line-height: 1.05; }
  .plan--basic { left: 30px; }
  .plan--business { left: 164px; }
  .plan--luxury { left: 292px; }
  .about {
    position: absolute; left: 445px; top: 505px; width: 714px;
    color: var(--white);
  }
  .about-title {
    text-align: center; font-family: "Montserrat", sans-serif; font-weight: 800;
    font-size: 24px; color: var(--ink); margin-bottom: 6px;
  }
  .about-title span { color: var(--white); }
  .about-text { font-size: 19px; line-height: 1.27; text-align: justify; }
  .features {
    position: absolute; left: 560px; top: 653px; width: 471px; height: 38px;
    background: var(--white); border: 3px solid var(--orange-light); border-radius: 20px;
    display: flex; align-items: center; justify-content: center; gap: 34px;
    font-weight: 700; font-size: 19px; color: var(--ink);
  }
  .features li { list-style: none; display: flex; align-items: center; gap: 12px; }
  .features li::before {
    content: ""; width: 12px; height: 12px; border-radius: 50%; background: var(--yellow-dot);
  }
  .cta {
    position: absolute; left: 470px; top: 727px; width: 690px;
    font-family: "Oswald", sans-serif;
  }
  .cta-line { display: flex; align-items: center; }
  .cta-label { font-size: 24px; font-weight: 600; color: var(--ink); width: 260px; text-align: center; }
  .cta-phone { font-size: 44px; font-weight: 700; color: var(--ink); margin-left: 14px; line-height: 1; }
  .icon { width: 34px; height: 34px; margin-left: 8px; }
  .web-line { display: flex; align-items: center; margin-top: 4px; font-family: "Lato", sans-serif; }
  .web-label { font-size: 18px; font-weight: 700; color: var(--white); width: 260px; text-align: center; }
  .web-icon { width: 20px; height: 20px; margin-left: 22px; }
  .web-url { font-size: 24px; font-weight: 700; color: var(--ink); margin-left: 18px; }
</style>
</head>
<body>
<main class="flyer">
  <svg class="flyer-shapes" viewBox="0 0 1200 816" width="1200" height="816">
    <defs>
      <linearGradient id="blueFill" x1="0" y1="0" x2="1" y2="0">
        <stop offset="0" stop-color="#2a68b5"/>
        <stop offset="0.45" stop-color="#6aa6de"/>
        <stop offset="1" stop-color="#2761ad"/>
      </linearGradient>
      <linearGradient id="orangeFill" x1="0" y1="1" x2="1" y2="0">
        <stop offset="0" stop-color="#f7a21e"/>
        <stop offset="1" stop-color="#f48a1a"/>
      </linearGradient>
      <linearGradient id="photoTone" x1="0" y1="0" x2="1" y2="1">
        <stop offset="0" stop-color="#8b95a3"/>
        <stop offset="0.45" stop-color="#dcdfe4"/>
        <stop offset="1" stop-color="#9aa7b7"/>
      </linearGradient>
      <linearGradient id="carTone" x1="0" y1="0" x2="0" y2="1">
        <stop offset="0" stop-color="#f4f5f6"/>
        <stop offset="0.6" stop-color="#d9dcdf"/>
        <stop offset="1" stop-color="#8e9296"/>
      </linearGradient>
      <radialGradient id="silver" cx="0.4" cy="0.3" r="0.8">
        <stop offset="0" stop-color="#ffffff"/>
        <stop offset="0.5" stop-color="#b9bcc0"/>
        <stop offset="1" stop-color="#6d7075"/>
      </radialGradient>
      <radialGradient id="gold" cx="0.4" cy="0.3" r="0.8">
        <stop offset="0" stop-color="#fff3c4"/>
        <stop offset="0.5" stop-color="#d6aa45"/>
        <stop offset="1" stop-color="#8a6517"/>
      </radialGradient>
    </defs>

    <path d="M0,330 C300,300 800,250 1200,240 L1200,816 L0,816 Z" fill="url(#blueFill)"/>

    <path d="M492,0 L1200,0 L1200,340 C1000,240 700,225 455,262 Z" fill="var(--blue)"/>
    <path role="img" aria-label="Photo: smiling couple seated in a rental car" d="M519,0 L1200,0 L1200,328 C1000,236 720,222 485,252 Z" fill="url(#photoTone)"/>

    <path d="M0,355 C300,330 600,268 900,262 C1030,260 1130,300 1200,345 L1200,465 C900,505 600,480 0,350 Z" fill="var(--white)"/>
    <path d="M0,0 L492,0 L455,262 C300,290 150,320 0,330 Z" fill="var(--white)"/>

    <rect role="img" aria-label="Photo: white two-door coupe" x="94" y="200" width="506" height="232" rx="36" fill="url(#carTone)"/>

    <path d="M34,364 L398,364 L398,600 Q398,627 371,627 L61,627 Q34,627 34,600 Z" fill="url(#orangeFill)" stroke="var(--white)" stroke-width="3"/>

    <g>
      <circle cx="88" cy="712" r="58" fill="url(#silver)" stroke="#ffffff" stroke-width="3"/>
      <circle cx="88" cy="712" r="47" fill="none" stroke="#8e9196" stroke-width="2"/>
      <circle cx="222" cy="712" r="58" fill="url(#silver)" stroke="#ffffff" stroke-width="3"/>
      <circle cx="222" cy="712" r="47" fill="none" stroke="#8e9196" stroke-width="2"/>
      <circle cx="350" cy="712" r="58" fill="url(#gold)" stroke="#ffffff" stroke-width="3"/>
      <circle cx="350" cy="712" r="47" fill="none" stroke="#9b7421" stroke-width="2"/>
    </g>

    <path d="M429,816 C445,735 520,703 610,703 L990,703 C1090,703 1150,750 1159,816 Z" fill="url(#orangeFill)" stroke="var(--white)" stroke-width="3"/>
  </svg>

  <div class="brand-name">Kestrel Lane</div>

  <h1 class="headline">RENT A CAR</h1>
  <p class="subhead">THE BEST CAR RENT SERVICE</p>

  <section class="offer">
    <p class="offer-title">SPECIAL OFFER</p>
    <div class="offer-deal">
      <span class="offer-percent">20%</span>
      <span class="offer-off">OFF</span>
      <span class="offer-period">FOR THIS<br>MONTH</span>
    </div>
  </section>

  <div class="plan plan--basic"><p class="plan-name">BASIC</p><p class="plan-price">$15</p></div>
  <div class="plan plan--business"><p class="plan-name">BUSINESS</p><p class="plan-price">$25</p></div>
  <div class="plan plan--luxury"><p class="plan-name">LUXURY</p><p class="plan-price">$30</p></div>

  <section class="about">
    <h2 class="about-title">ABOUT <span>US</span></h2>
    <p class="about-text">Been in a not at fault accident? We keep you on the road with a replacement hire car while your own vehicle is being repaired. We deal with the other party's insurer and bring a late model car right to your door. When you call us, please tell us where you got this flyer.</p>
  </section>

  <ul class="features">
    <li>Free delivery</li>
    <li>Late model/ New Model</li>
  </ul>

  <section class="cta">
    <div class="cta-line">
      <span class="cta-label">CALL NOW FOR BOOKING</span>
      <svg class="icon" viewBox="0 0 24 24" aria-hidden="true"><path d="M6.6 10.8c1.4 2.8 3.8 5.2 6.6 6.6l2.2-2.2c.3-.3.7-.4 1-.2 1.1.4 2.3.6 3.6.6.6 0 1 .4 1 1V20c0 .6-.4 1-1 1C10.6 21 3 13.4 3 4c0-.6.4-1 1-1h3.5c.6 0 1 .4 1 1 0 1.3.2 2.5.6 3.6.1.3 0 .7-.2 1z" fill="#ffffff"/></svg>
      <span class="cta-phone">1800 417 582</span>
    </div>
    <div class="web-line">
      <span class="web-label">Visit Us fot more information :</span>
      <svg class="web-icon" viewBox="0 0 20 20" aria-hidden="true"><circle cx="10" cy="10" r="8.5" fill="none" stroke="#1c1c1c" stroke-width="2"/><ellipse cx="10" cy="10" rx="3.5" ry="8.5" fill="none" stroke="#1c1c1c" stroke-width="1.6"/><line x1="1.5" y1="10" x2="18.5" y2="10" stroke="#1c1c1c" stroke-width="1.6"/></svg>
      <span class="web-url">www.kestrellane.com.au</span>
    </div>
  </section>
</main>
</body>
</html>
```